Zielgruppe
Steuerberatung
Aufgabenstellung
Ich benötige eine Neuerstellung für ein vorhandenes Briefpapier. Bedeutet, eigentlich soll der aktuelle Inhalt neu erstellt werden, da mir die Rohdaten nicht mehr zur Verfügung stehen. Das aktuelle Briefpapier steht als .doc zur Verfügung. Ziel 1:1 Abbildung. Zudem muss die Adresse geändert werden.

```html
<!DOCTYPE html>
<html lang="de">
<head>
<meta charset="utf-8">
<title>Briefpapier Lukas Brenner</title>
<link rel="stylesheet" href="https://fonts.googleapis.com/css2?family=Roboto+Condensed:wght@400;700&display=swap">
<style>
  :root {
    --backdrop: #000000;
    --paper: #ffffff;
    --ink: #111111;
    --watermark: #d9dadb;
  }
  html, body {
    margin: 0;
    padding: 0;
    width: 1200px;
    height: 2400px;
    overflow: hidden;
    background: var(--backdrop);
    font-family: "Roboto Condensed", "Arial Narrow", sans-serif;
    color: var(--ink);
  }
  .sheet {
    position: absolute;
    left: 192px;
    width: 816px;
    height: 1155px;
    background: var(--paper);
    overflow: hidden;
  }
  .sheet--first { top: 36px; }
  .sheet--follow { top: 1206px; }

  .brand-frame {
    position: absolute;
    left: 592px;
    top: 64px;
    width: 61px;
    height: 95px;
    border: 1px solid var(--ink);
    box-sizing: border-box;
    display: flex;
    align-items: center;
    justify-content: center;
    font-weight: 700;
    font-size: 13px;
  }
  .letterhead {
    position: absolute;
    left: 592px;
    top: 170px;
    font-size: 12.5px;
    line-height: 16.5px;
  }
  .letterhead strong { font-weight: 700; }
  .contact-list { list-style: none; margin: 0; padding: 0; }
  .contact-list li { display: flex; align-items: center; gap: 7px; }
  .contact-list svg { width: 11px; height: 11px; flex: none; }

  .return-address {
    position: absolute;
    left: 77px;
    top: 172px;
    font-size: 8.5px;
  }
  .return-address strong { font-weight: 700; }

  .watermark {
    position: absolute;
    left: 540px;
    top: 860px;
    display: flex;
    align-items: center;
    gap: 14px;
    color: var(--watermark);
    font-weight: 700;
    font-size: 120px;
    line-height: 1;
    white-space: nowrap;
  }
  .watermark__dot {
    width: 90px;
    height: 90px;
    border-radius: 50%;
    background: var(--watermark);
    flex: none;
  }
  .sheet--follow .watermark { top: 860px; }

  .legal-footer {
    position: absolute;
    left: 77px;
    top: 1067px;
    font-size: 11.6px;
    line-height: 16.5px;
    white-space: nowrap;
  }
  .legal-footer strong { font-weight: 700; }
</style>
</head>
<body>

<section class="sheet sheet--first">
  <div class="watermark"><span class="watermark__dot"></span><span>Brenner</span></div>

  <div class="brand-frame">Brenner</div>

  <div class="letterhead">
    <div><strong>Lukas Brenner</strong> | Steuerberater</div>
    <ul class="contact-list">
      <li>
        <svg viewBox="0 0 12 12"><circle cx="6" cy="6" r="6" fill="#111"/><rect x="4.3" y="2.5" width="3.4" height="7" rx="0.6" fill="#fff"/></svg>
        +49 (0) 170 . 00 12 345
      </li>
      <li>
        <svg viewBox="0 0 12 12"><circle cx="6" cy="6" r="6" fill="#111"/><path d="M3.2 4.2q0-1 1-1h3.6q1 0 1 1v0.6H7.4V4.2H4.6v0.6H3.2zM3.6 5.6h4.8v2.8H3.6z" fill="#fff"/></svg>
        +49 (0) 500 . 12 34 56 78
      </li>
      <li>
        <svg viewBox="0 0 12 12"><circle cx="6" cy="6" r="6" fill="#111"/><rect x="2.8" y="3.8" width="6.4" height="4.4" fill="#fff"/><path d="M2.8 3.8L6 6.4 9.2 3.8" stroke="#111" stroke-width="0.8" fill="none"/></svg>
        info@steuerberatung-brenner.de
      </li>
      <li>
        <svg viewBox="0 0 12 12"><circle cx="6" cy="6" r="5.5" fill="none" stroke="#111" stroke-width="1"/><ellipse cx="6" cy="6" rx="2.3" ry="5.5" fill="none" stroke="#111" stroke-width="0.8"/><path d="M0.5 6h11M1.4 3.5h9.2M1.4 8.5h9.2" stroke="#111" stroke-width="0.8"/></svg>
        www.steuerberatung-brenner.de
      </li>
    </ul>
  </div>

  <div class="return-address"><strong>Lukas Brenner</strong> | Lindenallee 18 | 30161 Nordstadt</div>

  <footer class="legal-footer">
    <div><strong>Lukas Brenner</strong> | Steuerberater</div>
    <div>Lindenallee 18 | 30161 Nordstadt | Zuständige Aufsichtsbehörde: Steuerberaterkammer Nordland · Körperschaft des öffentlichen Rechts</div>
    <div>Zuständiges Finanzamt: Finanzamt Nordstadt-Mitte · Steuernummer: 00/000/12345 | Bankverbindung: DE 00 1234 5678 9012 3456 78 BIC: NORDDEXX</div>
  </footer>
</section>

<section class="sheet sheet--follow">
  <div class="watermark"><span class="watermark__dot"></span><span>Brenner</span></div>

  <div class="brand-frame">Brenner</div>

  <div class="letterhead">
    <div><strong>Lukas Brenner</strong> | Steuerberater</div>
  </div>
</section>

</body>
</html>
```